Expensive Jewelery and Gold Website

I require a one page template design for my site PrimeIngotHouse.example. We sell replica gold bars. Not real ones, they are novelty gifts.

I have several images of the bars (attached)
I would like a stylish and professional template layout that will be used on my site.

Designed to appear to businesses and professionals and not the members of the public.

There is no idenity or artwork for the business so you may use whichever scheme you wish to. But must somehow stylish use the images or 2-3 of the images attached.

Target Market(s)

Business and marketing professional.

Industry/Entity Type

Business

Requirements
Must have
• Incorporate some or all of images
Nice to have
• Colour/styled images to match design and look in-keeping

```html
<!DOCTYPE html>
<html lang="en">
<head>
<meta charset="utf-8">
<title>PrimeIngotHouse.example</title>
<link rel="stylesheet" href="https://fonts.googleapis.com/css2?family=Gelasio:wght@400;600&family=PT+Sans:wght@400;700&display=swap">
<style>
  :root {
    --wood-dark: #8e3b17;
    --wood: #b9562a;
    --wood-light: #c8683a;
    --gold: #f6ad12;
    --gold-deep: #e39a05;
    --ink: #000;
    --panel: #ececec;
    --field-border: #b8b8b8;
    --paper: #fff;
    --footer: #3f2a02;
    --footer-rule: #6a4a10;
    --footer-muted: #9a7530;
    --dots: #c98a2a;
  }
  * { box-sizing: border-box; margin: 0; padding: 0; }
  html, body { width: 1200px; height: 844px; overflow: hidden; background: var(--ink); }
  .page { position: relative; width: 1200px; height: 844px; overflow: hidden; font-family: "Gelasio", Georgia, serif; }

  .masthead {
    position: absolute; left: 0; top: 0; width: 1200px; height: 379px;
    background: linear-gradient(90deg, var(--wood-dark) 0%, var(--wood) 18%, var(--wood-light) 40%, var(--wood) 62%, var(--wood-light) 82%, var(--wood-dark) 100%);
    border-bottom: 2px dotted var(--dots);
  }
  .brand-tab {
    position: absolute; left: 173px; top: 0; width: 89px; height: 112px;
    background: linear-gradient(180deg, #ffc84a, var(--gold-deep));
    border: 1px solid #ffe39a; border-top: none; border-radius: 0 0 4px 4px; z-index: 2;
  }
  .brand-name {
    position: absolute; left: 268px; top: 32px;
    font-family: "PT Sans", Arial, sans-serif; font-weight: 700; font-size: 34px;
    color: var(--paper); letter-spacing: -0.3px;
  }

  .showcase {
    position: absolute; left: 145px; top: 84px; width: 910px; height: 237px;
    background: var(--ink); border-radius: 4px; box-shadow: 0 2px 6px rgba(0,0,0,.6);
  }
  .showcase .photo {
    position: absolute; top: 11px; height: 216px; border: 1px solid #ddd; border-radius: 2px;
  }
  .photo-1 { left: 11px; width: 296px; background: linear-gradient(135deg, #5a2a10, #2a1408 45%, #b48a3a 55%, #6b3614); }
  .photo-2 { left: 308px; width: 295px; background: radial-gradient(ellipse at 50% 50%, #e8e8e6, #b8b6b2 55%, #6e6a64); }
  .photo-3 { left: 604px; width: 295px; background: linear-gradient(160deg, #111 0%, #2a2a2a 35%, #8e5a2a 60%, #4a220c); }

  .main-nav { position: absolute; left: 395px; top: 322px; display: flex; gap: 4px; list-style: none; }
  .main-nav li {
    width: 90px; height: 28px; border: 1px solid #cfcfcf; border-top: none; border-radius: 0 0 3px 3px;
    background: linear-gradient(180deg, #3a3a3a, #050505);
    color: var(--paper); font-family: "PT Sans", Arial, sans-serif; font-size: 11.5px;
    text-align: center; line-height: 30px; letter-spacing: .3px;
  }
  .main-nav li.active { background: linear-gradient(180deg, #ffc43a, var(--gold-deep)); color: #1a1000; font-weight: 700; }

  .feedback {
    position: absolute; left: 142px; top: 386px; width: 207px; height: 353px; background: var(--panel);
    font-family: "PT Sans", Tahoma, sans-serif; font-size: 11.5px; color: #222;
  }
  .feedback-title {
    position: absolute; left: 8px; top: 8px; width: 202px; height: 33px; background: var(--gold);
    border-radius: 4px 0 0 4px; font-size: 19px; font-weight: 700; color: #1a1000;
    padding-left: 16px; line-height: 34px; letter-spacing: 1.5px;
  }
  .feedback label { position: absolute; left: 18px; }
  .feedback .field { position: absolute; left: 17px; width: 171px; height: 21px; background: linear-gradient(180deg, #f2f2f2, var(--paper)); border: 1px solid var(--field-border); }
  .feedback .btn {
    position: absolute; top: 315px; width: 63px; height: 20px; border-radius: 3px;
    background: linear-gradient(180deg, #ffc43a, var(--gold-deep)); text-align: center; line-height: 20px; color: #1a1000;
  }

  .content { position: absolute; left: 370px; top: 398px; width: 686px; color: var(--paper); font-size: 11.7px; line-height: 12.3px; }
  .content h1 { font-size: 16px; font-weight: 600; color: var(--gold); margin-bottom: 9px; }
  .content p { margin-bottom: 12px; }
  .content .split { position: relative; height: 155px; }
  .content .split p { width: 392px; }
  .content .inset {
    position: absolute; left: 403px; top: 2px; width: 283px; height: 138px; border: 1px solid #ddd; border-radius: 3px;
    background: linear-gradient(160deg, #5a2a10, #241208 40%, #a8823a 55%, #6b3614 75%, #3a1a08);
  }

  .site-footer {
    position: absolute; left: 0; top: 746px; width: 1200px; height: 98px; background: var(--footer);
    border-top: 2px dotted var(--dots); font-family: "PT Sans", Tahoma, sans-serif;
  }
  .footer-nav { position: absolute; left: 0; width: 1200px; top: 22px; display: flex; justify-content: center; gap: 10px; list-style: none; color: var(--paper); font-size: 12.5px; }
  .footer-nav li::before { content: "•"; margin-right: 5px; font-size: 9px; vertical-align: 2px; }
  .footer-rule { position: absolute; left: 169px; top: 52px; width: 872px; height: 1px; background: linear-gradient(90deg, transparent, var(--footer-rule) 15%, var(--footer-rule) 85%, transparent); }
  .copyright { position: absolute; left: 0; width: 1200px; top: 60px; text-align: center; color: var(--footer-muted); font-size: 12.5px; }
</style>
</head>
<body>
<div class="page">
  <header class="masthead">
    <div class="brand-tab"></div>
    <div class="brand-name">PrimeIngotHouse.example</div>
    <div class="showcase">
      <div class="photo photo-1" role="img" aria-label="Gold bar presented in an open polished wooden box"></div>
      <div class="photo photo-2" role="img" aria-label="Gift box wrapped in silver paper with a ribbon bow"></div>
      <div class="photo photo-3" role="img" aria-label="Gold bar in a clear case inside a wooden presentation box"></div>
    </div>
    <ul class="main-nav">
      <li class="active">WELCOME</li>
      <li>ABOUT US</li>
      <li>SERVICES</li>
      <li>GALLERY</li>
      <li>LOCATED</li>
    </ul>
  </header>

  <aside class="feedback">
    <div class="feedback-title">FEED BACK</div>
    <label style="top:61px">Name:</label>
    <div class="field" style="top:72px"></div>
    <label style="top:109px">Email:</label>
    <div class="field" style="top:120px"></div>
    <label style="top:157px">Subject:</label>
    <div class="field" style="top:168px"></div>
    <label style="top:204px">Message:</label>
    <div class="field" style="top:215px;height:86px"></div>
    <div class="btn" style="left:18px">Send</div>
    <div class="btn" style="left:124px">Clear</div>
  </aside>

  <main class="content">
    <h1>Welcome to PrimeIngotHouse.example</h1>
    <p>Lorem Ipsum is simply dummy text of the printing and typesetting industry. Lorem Ipsum has been the industry's standard dummy text ever since the 1500s, when an unknown printer took a galley of type and scrambled it to make a type specimen book. It has survived not only five centuries, but also the leap into electronic typesetting, remaining essentially unchanged. It was popularised in the 1960s with the release of Letraset sheets containing Lorem Ipsum passages, and more recently with desktop publishing software like Aldus PageMaker including versions of Lorem Ipsum.</p>
    <div class="split">
      <p>Lorem Ipsum is simply dummy text of the printing and typesetting industry. Lorem Ipsum has been the industry's standard dummy text ever since the 1500s, when an unknown printer took a galley of type and scrambled it to make a type specimen book. It has survived not only five centuries, but also the leap into electronic typesetting, remaining essentially unchanged. It was popularised in the 1960s with the release of Letraset sheets containing Lorem Ipsum passages, and more recently with desktop publishing software like Aldus PageMaker including versions of Lorem Ipsum.</p>
      <div class="inset" role="img" aria-label="Gold bar resting in an open wooden gift case"></div>
    </div>
    <p>Lorem Ipsum is simply dummy text of the printing and typesetting industry. Lorem Ipsum has been the industry's standard dummy text ever since the 1500s, when an unknown printer took a galley of type and scrambled it to make a type specimen book. It has survived not only five centuries, but also the leap into electronic typesetting, remaining essentially unchanged. It was popularised in the 1960s with the release of Letraset sheets containing Lorem Ipsum passages, and more recently with desktop publishing software like Aldus PageMaker including versions of Lorem Ipsum.</p>
  </main>

  <footer class="site-footer">
    <ul class="footer-nav">
      <li>Home</li><li>About Us</li><li>Services</li><li>Gallery</li><li>Located</li>
    </ul>
    <div class="footer-rule"></div>
    <div class="copyright">Copyright © 2010 &nbsp;PrimeIngotHouse.example</div>
  </footer>
</div>
</body>
</html>
```